3 out of 100 people will get deadly skin cancer - we need a great illustration that shows this!

We put together a prototype image that communicates lifetime skin cancer risk. (see attached). We are looking for illustrators who can take make a new/better/cooler graphic that communicates this idea. It could be as simple as a superior illustration of the graphic we have or illustrators can propose a completely different idea.What should the illustration communicate?U.S. adults have a lifetime risk of developing skin cancer of 1 in 5. But we don't want to show 1 in 5; we want to show that number in a larger group. For example, in the attached illustration we show 20 in 100 people get skin cancer (i.e., 100 beach towels/umbrellas and 20 of them are red). Research has shown that people are more likely to accurately understand numbers like this when you convey them for larger groups (i.e., 20 out of 100 rather than 1 out of 5). U.S. adults also have a lifetime risk of 2.3% of developing the deadliest form of skin cancer (melanoma). In other words, approximately 3 in 100 people will develop melanoma in their lifetime. Ideally, a single image will convey both lifetime skin cancer risk (20 in 100) and melanoma risk (3 in 100). We will award a top three as follows: 1st place = $300, 2nd place = $250, third place = $200. We will also buy any design beyond 3rd place that we like for $100. For example, we purchased 24 designs in our last contest on Artmarketly.This research is supported by funding from the Corvane Institute of Science.

Target Market(s)

The U.S. public; individuals at high risk of developing skin cancer

Industry/Entity Type

Medicine

Colors

Designer to choose colors to be used in the design.

Requirements
Must have
• an original illustration that conveys both lifetime risk of developing skin cancer (20 in 100) and melanoma (3 in 100).
Nice to have
• It can be beach towels and umbrellas, just like our prototype, or the designers can pitch an original idea. Imagery can be realistic or cartoonish (or something in between). It should be illustrations, though. Not edited photos. The image should be in color (no black and white illustrations).
Should not have
• Photos. Clip art. Free vector images.
• We are looking for original illustrations created by the designer.

```html
<!DOCTYPE html>
<html lang="en">
<head>
<meta charset="utf-8">
<title>Lifetime Skin Cancer Risk</title>
<link rel="stylesheet" href="https://fonts.googleapis.com/css2?family=Roboto:wght@400;500;700;900&display=swap">
<style>
  :root {
    --skin-light: #f8cbb0;
    --skin-dark: #e4ab84;
    --title-blue: #1d6fbd;
    --safe-blue: #2d68b8;
    --cancer-red: #c7222f;
    --melanoma-maroon: #4e120e;
    --sea-blue: #29a8e0;
    --white: #ffffff;
  }
  * { margin: 0; padding: 0; box-sizing: border-box; }
  html, body { width: 848px; height: 1200px; overflow: hidden; }
  body { font-family: "Roboto", Arial, sans-serif; background: var(--skin-light); }
  .poster { position: relative; width: 848px; height: 1200px; overflow: hidden; }
  .backdrop {
    position: absolute; inset: 0;
    background:
      radial-gradient(ellipse 420px 620px at 424px 640px, var(--skin-light) 70%, transparent 71%),
      linear-gradient(180deg, var(--skin-dark) 0%, var(--skin-light) 14%, var(--skin-light) 45%, var(--skin-dark) 100%);
  }
  .title {
    position: absolute; top: 26px; left: 0; width: 100%; text-align: center;
    font-weight: 900; font-size: 41px; letter-spacing: 0.5px; color: var(--title-blue);
    text-shadow: 3px 3px 0 var(--white);
  }
  .subtitle {
    position: absolute; top: 82px; left: 100px; width: 643px; height: 47px;
    background: var(--white); color: var(--title-blue);
    font-size: 31px; font-weight: 400; text-align: center; line-height: 47px;
  }
  .beach-grid { position: absolute; display: grid; gap: 0; }
  .beach-grid.upper { top: 170px; left: 20px; grid-template-columns: repeat(12, 66px); grid-auto-rows: 81px; }
  .beach-grid.lower { top: 575px; left: 152px; grid-template-columns: repeat(8, 66px); grid-auto-rows: 81px; }
  .person { position: relative; width: 66px; height: 81px; }
  .person::before {
    content: ""; position: absolute; left: 2px; top: 0; width: 50px; height: 50px; border-radius: 50%;
    background: radial-gradient(circle at 40% 35%, rgba(255,255,255,0.45), transparent 60%), var(--safe-blue);
  }
  .person::after {
    content: ""; position: absolute; left: 20px; top: 38px; width: 30px; height: 40px; border-radius: 3px;
    background: var(--safe-blue); opacity: 0.55; transform: skewX(-25deg);
  }
  .person.cancer::before { background-color: var(--cancer-red); }
  .person.cancer::after { background: var(--cancer-red); }
  .person.melanoma::before { background-color: #a01e22; }
  .person.melanoma::after { background: var(--melanoma-maroon); opacity: 0.9; }
  .footer-wave { position: absolute; left: 0; top: 990px; width: 848px; height: 210px; }
  .legend { position: absolute; left: 70px; top: 1042px; list-style: none; }
  .legend li {
    display: flex; align-items: center; height: 46px; color: var(--white);
    font-weight: 700; font-size: 13.5px;
  }
  .legend .swatch {
    width: 40px; height: 40px; border-radius: 50%; background: var(--white);
    display: flex; align-items: center; justify-content: center; margin-right: 13px;
  }
  .legend .swatch span { width: 26px; height: 26px; border-radius: 50%; background: var(--safe-blue); }
  .legend .swatch.cancer span { background: var(--cancer-red); }
  .legend .swatch.melanoma span { background: var(--melanoma-maroon); }
  .explainer { position: absolute; left: 463px; top: 1098px; width: 350px; color: var(--white); font-size: 12.5px; line-height: 15px; }
  .explainer strong { display: block; font-weight: 700; font-size: 13px; margin-bottom: 4px; }
</style>
</head>
<body>
<main class="poster">
  <div class="backdrop" role="img" aria-label="Illustrated back of a sunbathing person in skin tones"></div>

  <h1 class="title">LIFETIME SKIN CANCER RISK</h1>
  <p class="subtitle">How likely are you to get skin cancer?</p>

  <section class="beach-grid upper" aria-label="First 60 beachgoers">
    <div class="person"></div><div class="person"></div><div class="person"></div><div class="person melanoma"></div><div class="person"></div><div class="person"></div><div class="person"></div><div class="person cancer"></div><div class="person"></div><div class="person"></div><div class="person"></div><div class="person"></div>
    <div class="person"></div><div class="person"></div><div class="person"></div><div class="person"></div><div class="person"></div><div class="person cancer"></div><div class="person"></div><div class="person"></div><div class="person"></div><div class="person"></div><div class="person cancer"></div><div class="person"></div>
    <div class="person"></div><div class="person cancer"></div><div class="person"></div><div class="person cancer"></div><div class="person"></div><div class="person"></div><div class="person"></div><div class="person"></div><div class="person cancer"></div><div class="person"></div><div class="person"></div><div class="person"></div>
    <div class="person"></div><div class="person"></div><div class="person"></div><div class="person"></div><div class="person cancer"></div><div class="person"></div><div class="person"></div><div class="person"></div><div class="person"></div><div class="person"></div><div class="person"></div><div class="person"></div>
    <div class="person"></div><div class="person cancer"></div><div class="person"></div><div class="person"></div><div class="person"></div><div class="person"></div><div class="person melanoma"></div><div class="person"></div><div class="person"></div><div class="person cancer"></div><div class="person"></div><div class="person"></div>
  </section>

  <section class="beach-grid lower" aria-label="Remaining 40 beachgoers">
    <div class="person cancer"></div><div class="person"></div><div class="person"></div><div class="person"></div><div class="person"></div><div class="person cancer"></div><div class="person"></div><div class="person"></div>
    <div class="person"></div><div class="person"></div><div class="person cancer"></div><div class="person"></div><div class="person"></div><div class="person"></div><div class="person"></div><div class="person cancer"></div>
    <div class="person"></div><div class="person"></div><div class="person"></div><div class="person"></div><div class="person cancer"></div><div class="person"></div><div class="person"></div><div class="person"></div>
    <div class="person melanoma"></div><div class="person"></div><div class="person"></div><div class="person"></div><div class="person"></div><div class="person"></div><div class="person"></div><div class="person cancer"></div>
    <div class="person"></div><div class="person"></div><div class="person cancer"></div><div class="person"></div><div class="person"></div><div class="person cancer"></div><div class="person"></div><div class="person"></div>
  </section>

  <svg class="footer-wave" viewBox="0 0 848 210" aria-hidden="true">
    <path d="M0,38 C180,70 420,72 620,48 C720,36 790,18 848,2 L848,210 L0,210 Z" fill="var(--white)"/>
    <path d="M0,48 C180,80 420,82 620,58 C720,46 790,28 848,14 L848,210 L0,210 Z" fill="var(--sea-blue)"/>
  </svg>

  <ul class="legend">
    <li><span class="swatch"><span></span></span>NO SKIN CANCER</li>
    <li><span class="swatch cancer"><span></span></span>SKIN CANCER</li>
    <li><span class="swatch melanoma"><span></span></span>MELANOMA</li>
  </ul>

  <div class="explainer">
    <strong>LET’S SAY 100 PEOPLE GO TO THE BEACH...</strong>
    How many will develop skin cancer in their lifetime?<br>
    How many will develop melanoma, the deadliest form of skin cancer?
  </div>
</main>
</body>
</html>
```